Logo & Visitenkarte für Immobilienunternehmen
Zielgruppe
Wir sind ein Immobilienunternehmen. Wir sind tätig im Immobilienhandel, der Immobilienvermittlung und der Erstellung von Häusern.
Unsere Zielgruppe sind Personen, die eine Immobilie kaufen oder verkaufen wollen. Personen ab ca. 30 Jahren mit mittlerem bis hohem Kapital bzw. Einkommen
Aufgabenstellung
Das Design soll für Sicherheit, Vertrauen, Seriosität, Professionalität und Hochwertigkeit stehen, da es in der Immobilienbranche oft um sehr viel Geld geht.

```html
<!DOCTYPE html>
<html lang="de">
<head>
<meta charset="utf-8">
<title>Ferbin Immobilien – Visitenkarte</title>
<link rel="stylesheet" href="https://fonts.googleapis.com/css2?family=Jost:wght@400;500&display=swap">
<style>
  :root {
    --stage-light: #f4f4f4;
    --stage-dark: #d2d2d2;
    --card-grey: #7d796f;
    --accent-gold: #f2ae2c;
    --text-on-band: #6f6a60;
    --card-shadow: rgba(0, 0, 0, 0.25);
  }
  * { box-sizing: border-box; margin: 0; padding: 0; }
  html, body { width: 1200px; height: 675px; overflow: hidden; }
  body {
    background: radial-gradient(ellipse at 45% 40%, var(--stage-light) 0%, var(--stage-dark) 100%);
    font-family: "Jost", Arial, sans-serif;
    position: relative;
  }
  .card {
    position: absolute;
    top: 192px;
    width: 500px;
    height: 290px;
    background: var(--card-grey);
    box-shadow: 0 10px 24px var(--card-shadow);
    color: var(--accent-gold);
  }
  .card--front { left: 70px; }
  .card--back { left: 630px; }

  .brand {
    position: absolute;
    left: 0; right: 0;
    text-align: center;
    font-weight: 500;
    letter-spacing: 0.18em;
    color: var(--accent-gold);
    white-space: nowrap;
  }
  .card--front .brand { top: 130px; font-size: 24px; }
  .card--back .brand { top: 48px; font-size: 19px; }
  .brand__mark {
    display: inline-block;
    width: 0.6em; height: 0.6em;
    background: var(--accent-gold);
    margin-right: 0.55em;
    vertical-align: 0.05em;
  }

  .name-band {
    position: absolute;
    left: 0; top: 122px;
    width: 305px; height: 34px;
    background: var(--accent-gold);
    color: var(--text-on-band);
    font-size: 17px;
    font-weight: 500;
    letter-spacing: 0.04em;
    line-height: 34px;
    padding-left: 95px;
    text-transform: uppercase;
  }

  .address {
    position: absolute;
    left: 82px; top: 192px;
    display: flex; align-items: center; gap: 16px;
    font-size: 14px; line-height: 1.35;
  }
  .contact {
    position: absolute;
    left: 322px; top: 112px;
    font-size: 12.5px;
    list-style: none;
  }
  .contact li { display: flex; align-items: center; gap: 10px; margin-bottom: 6px; }
  .icon { flex: none; }
</style>
</head>
<body>
  <section class="card card--front" aria-label="Vorderseite">
    <p class="brand"><span class="brand__mark"></span>FERBIN IMMOBILIEN</p>
  </section>

  <section class="card card--back" aria-label="Rückseite">
    <p class="brand"><span class="brand__mark"></span>FERBIN IMMOBILIEN</p>

    <p class="name-band">Lukas Ferbin</p>

    <div class="address">
      <svg class="icon" width="18" height="24" viewBox="0 0 18 24" aria-hidden="true">
        <path d="M9 1a8 8 0 0 0-8 8c0 6 8 14 8 14s8-8 8-14a8 8 0 0 0-8-8z" fill="var(--accent-gold)"/>
        <circle cx="9" cy="9" r="3" fill="var(--card-grey)"/>
      </svg>
      <p>Lindenweg 12<br>6048 Seedorf</p>
    </div>

    <ul class="contact">
      <li>
        <svg class="icon" width="14" height="14" viewBox="0 0 14 14" aria-hidden="true">
          <circle cx="7" cy="7" r="6" fill="none" stroke="var(--accent-gold)" stroke-width="1.2"/>
          <path d="M5 4.2c-.6.5-.6 1.6.3 3s2 2.4 2.9 2.4l.9-.8-1-1-.7.4-1.3-1.4.4-.7-1-1.1z" fill="var(--accent-gold)"/>
        </svg>
        <span>+41 79 410 27 58</span>
      </li>
      <li>
        <svg class="icon" width="14" height="11" viewBox="0 0 14 11" aria-hidden="true">
          <rect x="0.6" y="0.6" width="12.8" height="9.8" fill="none" stroke="var(--accent-gold)" stroke-width="1.2"/>
          <path d="M0.8 1l6.2 5 6.2-5" fill="none" stroke="var(--accent-gold)" stroke-width="1.2"/>
        </svg>
        <span>info@ferbin-immobilien.ch</span>
      </li>
    </ul>
  </section>
</body>
</html>
```